Silver Brook Constructions Ltd Stationary
business cards, stationary etc.
Silver Brook Constructions Ltd Stationary - Construction
Creative Brief
Simple
Dalton Wexford
4816 Ardmore Rd. Victoria B.C. V8N 4K7
250-384-6252 could we put this number under office instead of phone
222-222-2222 temporary until I get new number
dalton@silverbrookconstructions.example
www.silverbrookconstructions.example
We would like designs for business cards , envelopes, letterhead, thank-you cards with evelopes, fax cover sheet, and presentation folder. Thank you
information should be on the back of the card along with some clean lines and simplicity while keeping a very professional feel

```html
<!DOCTYPE html>
<html lang="en">
<head>
<meta charset="utf-8">
<title>Silver Brook Constructions Ltd – Business Cards</title>
<link href="https://fonts.googleapis.com/css2?family=Cinzel:wght@400;600&family=Montserrat:wght@500&family=Open+Sans:wght@400&display=swap" rel="stylesheet">
<style>
  :root {
    --board: #2f2f2f;
    --card-dark: #050505;
    --card-light: #ffffff;
    --green: #8fb43a;
    --green-deep: #6f9628;
    --green-light: #c3dc6a;
    --ink-light: #f2f2f2;
    --ink-dark: #2b2b2b;
    --muted: #8a8a8a;
    --label: #e8e8e8;
    --grey-mark: #6f7a7a;
  }
  * { margin: 0; padding: 0; box-sizing: border-box; }
  html, body { width: 1200px; height: 844px; overflow: hidden; }
  body { background: var(--board); position: relative; font-family: "Open Sans", sans-serif; }

  .card {
    position: absolute; width: 504px; height: 290px;
    border-radius: 16px; overflow: hidden;
  }
  .card--dark { background: var(--card-dark); color: var(--ink-light); }
  .card--light { background: var(--card-light); color: var(--ink-dark); }
  .pos-front-dark { left: 80px; top: 72px; }
  .pos-front-light { left: 619px; top: 72px; }
  .pos-back-dark { left: 80px; top: 450px; }
  .pos-back-light { left: 619px; top: 450px; }

  .label {
    position: absolute; width: 504px; text-align: center;
    font-family: "Montserrat", sans-serif; font-weight: 500;
    font-size: 19px; letter-spacing: 3px; font-variant: small-caps;
    color: var(--label);
  }
  .label--top { top: 375px; }
  .label--bottom { top: 774px; }
  .label--left { left: 80px; }
  .label--right { left: 619px; }

  .brand-dot {
    position: absolute; left: 50%; top: 26px; transform: translateX(-50%);
    width: 80px; height: 80px; border-radius: 50%;
    background: var(--green);
  }
  .brand-name {
    position: absolute; top: 150px; width: 100%; text-align: center;
    font-family: "Cinzel", serif; font-weight: 400;
    font-size: 32px; letter-spacing: 1px; line-height: 1;
  }
  .brand-sub {
    position: absolute; top: 187px; width: 100%; text-align: center;
    font-family: "Cinzel", serif; font-weight: 400;
    font-size: 14px; letter-spacing: 2px; line-height: 1;
  }
  .tagline {
    position: absolute; top: 204px; width: 100%; text-align: center;
    font-family: "Cinzel", serif; font-size: 8px; letter-spacing: 2px;
    color: var(--muted); line-height: 1;
  }
  .tagline::before {
    content: ""; display: block; width: 200px; height: 1px;
    margin: 0 auto 4px; background: var(--muted);
  }
  .person {
    position: absolute; top: 230px; width: 100%; text-align: center;
    font-family: "Cinzel", serif; font-size: 13px; letter-spacing: 1px;
    color: var(--muted); line-height: 1;
  }
  .swoosh { position: absolute; left: 0; bottom: 0; width: 504px; height: 42px; }

  .back-name {
    position: absolute; top: 104px; width: 100%; text-align: center;
    font-family: "Cinzel", serif; font-weight: 400;
    font-size: 46px; letter-spacing: 2px; line-height: 1;
  }
  .card--dark .back-name { color: var(--green); }
  .card--light .back-name { color: var(--grey-mark); }

  .contact {
    position: absolute; left: 0; width: 100%; text-align: center;
    font-size: 9.5px; line-height: 1; white-space: nowrap;
  }
  .contact--line1 { top: 216px; }
  .contact--line2 { top: 232px; }
  .contact span { margin: 0 5px; }
  .contact svg { width: 9px; height: 9px; vertical-align: -1px; margin-right: 3px; }
  .card--dark .contact svg { fill: var(--ink-light); }
  .card--light .contact svg { fill: var(--ink-dark); }
</style>
</head>
<body>

<section class="card card--dark pos-front-dark">
  <div class="brand-dot"></div>
  <div class="brand-name">SILVER BROOK</div>
  <div class="brand-sub">CONSTRUCTIONS LTD.</div>
  <div class="tagline">SUSTAINABILITY FOR EVERYONE</div>
  <div class="person">Dalton Wexford</div>
  <svg class="swoosh" viewBox="0 0 504 42" preserveAspectRatio="none">
    <path d="M0 16 Q252 -8 504 16 L504 42 L0 42 Z" fill="var(--green)"/>
    <path d="M0 16 Q252 -8 504 16 L504 20 Q252 -2 0 20 Z" fill="var(--green-light)"/>
    <path d="M0 30 Q252 16 504 30 L504 42 L0 42 Z" fill="var(--green-deep)"/>
  </svg>
</section>
<div class="label label--top label--left">Business Card Front</div>

<section class="card card--light pos-front-light">
  <div class="brand-dot"></div>
  <div class="brand-name">SILVER BROOK</div>
  <div class="brand-sub">CONSTRUCTIONS LTD.</div>
  <div class="tagline">SUSTAINABILITY FOR EVERYONE</div>
  <div class="person">Dalton Wexford</div>
  <svg class="swoosh" viewBox="0 0 504 42" preserveAspectRatio="none">
    <path d="M0 16 Q252 -8 504 16 L504 42 L0 42 Z" fill="var(--green)"/>
    <path d="M0 16 Q252 -8 504 16 L504 20 Q252 -2 0 20 Z" fill="#d9d9d9"/>
    <path d="M0 30 Q252 16 504 30 L504 42 L0 42 Z" fill="var(--green-deep)"/>
  </svg>
</section>
<div class="label label--top label--right">Business Card Front</div>

<section class="card card--dark pos-back-dark">
  <div class="back-name">SILVER BROOK</div>
  <div class="contact contact--line1">
    <span><svg viewBox="0 0 10 10"><path d="M2 0 L4 2 L3 3.5 Q4.5 5.5 6.5 7 L8 6 L10 8 L8.5 10 Q3 9 0 1.5 Z"/></svg>250-384-6252</span>
    <span><svg viewBox="0 0 10 10"><rect x="2.5" y="0" width="5" height="10" rx="1"/></svg>222-222-2222</span>
    <span><svg viewBox="0 0 10 10"><path d="M0 2 H10 V8 H0 Z"/></svg>dalton@silverbrookconstructions.example</span>
  </div>
  <div class="contact contact--line2">
    <span><svg viewBox="0 0 10 10"><circle cx="5" cy="5" r="5"/></svg>www.silverbrookconstructions.example</span>
    <span><svg viewBox="0 0 10 10"><path d="M5 0 A3.5 3.5 0 0 1 8.5 3.5 Q8.5 6 5 10 Q1.5 6 1.5 3.5 A3.5 3.5 0 0 1 5 0 Z"/></svg>4816 Ardmore Rd. Victoria B.C. V8N 4K7</span>
  </div>
</section>
<div class="label label--bottom label--left">Business Card Back</div>

<section class="card card--light pos-back-light">
  <div class="back-name">SILVER BROOK</div>
  <div class="contact contact--line1">
    <span><svg viewBox="0 0 10 10"><path d="M2 0 L4 2 L3 3.5 Q4.5 5.5 6.5 7 L8 6 L10 8 L8.5 10 Q3 9 0 1.5 Z"/></svg>250-384-6252</span>
    <span><svg viewBox="0 0 10 10"><rect x="2.5" y="0" width="5" height="10" rx="1"/></svg>222-222-2222</span>
    <span><svg viewBox="0 0 10 10"><path d="M0 2 H10 V8 H0 Z"/></svg>dalton@silverbrookconstructions.example</span>
  </div>
  <div class="contact contact--line2">
    <span><svg viewBox="0 0 10 10"><circle cx="5" cy="5" r="5"/></svg>www.silverbrookconstructions.example</span>
    <span><svg viewBox="0 0 10 10"><path d="M5 0 A3.5 3.5 0 0 1 8.5 3.5 Q8.5 6 5 10 Q1.5 6 1.5 3.5 A3.5 3.5 0 0 1 5 0 Z"/></svg>4816 Ardmore Rd. Victoria B.C. V8N 4K7</span>
  </div>
</section>
<div class="label label--bottom label--right">Business Card Back</div>

</body>
</html>
```